Castastrophe General Contractor needs leave behind for sales

Will respond quickly to designer inquires
Fast winning selection
Will notify all of winning selection

Catastrophe Restoration General Contractor offering specialized services to the insurance industry. Sales meeting leave behind flyer for presentation to insurance agents. We would like for agents to refer policyholders to our company for complete residential and commercial restoration projects.

Some copy uploaded for reference. 5.5" x 8.5" approx - double sided color w/ sales business card reproduced on back side. Approved / Preferred Contractor for Brightshield, Vantacover, KRPQ & Fenlo insurance companies.

Larkmoor Company is a general contractor specialized in the restoration industry for both residential and commercial properties.
We have incorporated the best technology tools and partnered with a network of industry professionals across the country to provide the most efficient and comprehensive service available.
Website under construction: www.thelarkmoorcompany.example

Target Market(s)

Insurance Sale Agents

Industry/Entity Type

Residential

Requirements
Must have
• Brightshield, Vantacover & KRPQ & Halvey Dresmit logos. Space to reproduce business card on back.. Looking for concept deign where we can work w/ local designer if necessary to finalize. Open to different sized flyer dependent on design.

```html
<!DOCTYPE html>
<html lang="en">
<head>
<meta charset="utf-8">
<title>Larkmoor Company – Agent Leave-Behind Flyer</title>
<link href="https://fonts.googleapis.com/css2?family=Open+Sans:wght@300;400;600;700;800&display=swap" rel="stylesheet">
<style>
  :root{
    --navy:#245a78;
    --navy-deep:#1d4a63;
    --orange:#f6b23e;
    --gold:#d9a441;
    --ink:#2f3a40;
    --paper:#ffffff;
    --stage:#e4e5e7;
    --line:#7f97a6;
  }
  *{box-sizing:border-box;margin:0;padding:0}
  html,body{width:1200px;height:1000px;overflow:hidden}
  body{background:var(--stage);font-family:"Open Sans",Arial,sans-serif;color:var(--ink);position:relative}

  .flyer{position:absolute;left:250px;width:700px;height:453px;background:var(--paper);box-shadow:0 6px 18px rgba(0,0,0,.12);overflow:hidden}
  .flyer--front{top:26px}
  .flyer--back{top:519px}

  /* front */
  .headline{position:absolute;left:30px;top:14px;color:var(--navy);line-height:1}
  .headline__lead{font-size:22px;font-weight:400;letter-spacing:.5px}
  .headline__key{font-size:32px;font-weight:800;letter-spacing:.5px}
  .headline__tail{font-size:32px;font-weight:300;letter-spacing:.5px}

  .support-panel{position:absolute;left:20px;top:110px;width:440px;height:282px;background:var(--navy);border-bottom-right-radius:26px;color:#fff;padding:10px 16px}
  .support-panel__corner{position:absolute;right:0;top:-30px;width:150px;height:110px}
  .support-panel__title{position:relative;font-size:12px;font-weight:700;line-height:1.3;max-width:300px}
  .support-panel__sub{font-size:11.5px;font-weight:700;margin-top:5px}
  .support-list{list-style:none;font-size:10.5px;line-height:1.35;margin-top:1px}
  .support-list li::before{content:"• "}

  .benefits{position:absolute;left:12px;top:124px;width:416px;height:148px;background:var(--orange);border-radius:22px;padding:6px 14px;color:var(--navy-deep)}
  .benefits__title{font-size:19px;font-weight:700;line-height:1.3}
  .benefit-row{display:flex;align-items:flex-start;margin-top:4px}
  .benefit-row__icon{width:18px;height:18px;border-radius:50%;background:var(--navy);flex:none;margin-right:8px}
  .benefit-row__name{width:130px;font-size:9.5px;font-weight:700;flex:none;line-height:1.2}
  .benefit-row__points{list-style:none;font-size:7.5px;line-height:1.3}
  .benefit-row__points li::before{content:"• "}

  .partner-row{position:absolute;left:22px;top:396px;width:440px;height:50px;display:flex;align-items:center;gap:12px;font-size:10.5px;font-weight:600;color:var(--ink)}
  .partner-badge{width:24px;height:24px;border-radius:50%;background:#6f7479;flex:none}

  .illustration{position:absolute;background:linear-gradient(160deg,#ffffff 0%,#e9ebed 35%,#8a8f93 55%,#a0714a 75%,#f2f2f2 100%)}
  .flyer--front .illustration{left:478px;top:150px;width:222px;height:230px}
  .flyer--back .illustration{left:560px;top:200px;width:140px;height:253px}

  .brand{position:absolute;display:flex;align-items:center;gap:8px;color:var(--gold);font-size:15px;font-weight:600;letter-spacing:1px;text-transform:uppercase;white-space:nowrap}
  .brand__mark{width:22px;height:22px;background:var(--navy)}
  .flyer--front .brand{right:24px;top:404px}
  .flyer--back .brand{left:34px;top:246px}

  /* back */
  .accent-square{position:absolute;left:150px;top:70px;width:58px;height:46px;background:var(--orange)}
  .accent-rule-h{position:absolute;left:120px;top:94px;width:30px;height:1px;background:var(--line)}
  .accent-rule-v{position:absolute;left:120px;top:94px;width:1px;height:136px;background:var(--line)}
  .about{position:absolute;left:222px;top:68px;width:320px;font-size:10.5px;line-height:1.45;color:var(--navy)}

  .contact{position:absolute;left:270px;top:236px;padding-left:16px;border-left:1px solid var(--line);color:var(--navy);font-size:12.5px;line-height:1.6}
  .contact__row{display:flex;align-items:center;gap:6px}
  .contact__row svg{width:12px;height:12px;flex:none}
  .contact__web{letter-spacing:2px;font-size:11px;white-space:nowrap}
</style>
</head>
<body>

<section class="flyer flyer--front" aria-label="Flyer front">
  <div class="headline">
    <div class="headline__lead">YOUR NATIONAL</div>
    <div class="headline__key">RESTORATION</div>
    <div class="headline__tail">CONTRACTOR</div>
  </div>

  <div class="support-panel">
    <svg class="support-panel__corner" viewBox="0 0 150 110" aria-hidden="true">
      <polygon points="150,0 150,110 20,110" fill="#f6b23e"/>
      <circle cx="106" cy="56" r="34" fill="#ffffff"/>
      <circle cx="106" cy="56" r="28" fill="#245a78"/>
    </svg>
    <p class="support-panel__title">Preferred Contractor Agent Support<br>Providing claims support during and after a CAT event</p>
    <p class="support-panel__sub">Agent Support Services</p>
    <ul class="support-list">
      <li>Guaranteed next day inspections from time of notification</li>
      <li>Damage status reporting directly back to Agent</li>
      <li>Assist policy holder in filing claim to CAT desk</li>
    </ul>

    <div class="benefits">
      <p class="benefits__title">Agent Benefits:</p>
      <div class="benefit-row">
        <span class="benefit-row__icon"></span>
        <span class="benefit-row__name">Greater Satisfaction, Increased Retention</span>
        <ul class="benefit-row__points">
          <li>Improve policyholder satisfaction</li>
          <li>Demonstrate commitment to customer care</li>
          <li>Follow up on claims through final billing</li>
        </ul>
      </div>
      <div class="benefit-row">
        <span class="benefit-row__icon"></span>
        <span class="benefit-row__name">Enhanced Efficiency</span>
        <ul class="benefit-row__points">
          <li>Increase efficiency from claim to completion</li>
          <li>Photo reports sent directly to the agent</li>
          <li>Reduce time agents spend on claim calls</li>
        </ul>
      </div>
      <div class="benefit-row">
        <span class="benefit-row__icon"></span>
        <span class="benefit-row__name">Increased Quality Control</span>
        <ul class="benefit-row__points">
          <li>Pre-screened and credentialed for licensing and insurance</li>
          <li>Consistent documentation and pricing standards</li>
          <li>Background-checked staff on every site</li>
        </ul>
      </div>
    </div>
  </div>

  <div class="partner-row">
    <span>Brightshield</span>
    <span>Vantacover</span>
    <span>KRPQ</span>
    <span class="partner-badge"></span>
    <span class="partner-badge"></span>
    <span>Fenlo</span>
    <span>Halvey Dresmit</span>
  </div>

  <div class="illustration" role="img" aria-label="Cutaway house model resting on architectural blueprints"></div>
  <div class="brand"><span class="brand__mark"></span>Larkmoor Company</div>
</section>

<section class="flyer flyer--back" aria-label="Flyer back">
  <span class="accent-rule-h"></span>
  <span class="accent-rule-v"></span>
  <span class="accent-square"></span>
  <p class="about">We are your best choice for complete renovation services. Larkmoor Company is a General Contractor tailored to the restoration industry for both residential and commercial properties. With operations currently established across 17 states, we have incorporated the best technology tools and partners.</p>

  <div class="brand"><span class="brand__mark"></span>Larkmoor Company</div>

  <div class="contact">
    <div class="contact__row">
      <svg viewBox="0 0 12 12" aria-hidden="true"><circle cx="6" cy="6" r="5.5" fill="none" stroke="#245a78"/><path d="M4 3.5l1 1.5-.6.7c.4.9 1 1.5 1.9 1.9l.7-.6 1.5 1-.6 1C5.5 8.8 3.2 6.5 3 4.1z" fill="#245a78"/></svg>
      <span>(800) 555-0142</span>
    </div>
    <div class="contact__row">
      <svg viewBox="0 0 12 12" aria-hidden="true"><rect x="1" y="2.5" width="10" height="7" fill="#245a78"/><path d="M1 2.5l5 4 5-4" fill="none" stroke="#fff"/></svg>
      <span>info@larkmoorcompany.example</span>
    </div>
    <div class="contact__web">www.thelarkmoorcompany.example</div>
  </div>

  <div class="illustration" role="img" aria-label="Cutaway house model resting on architectural blueprints"></div>
</section>

</body>
</html>
```